Business card for Eyelash extension salon in Marlow Hills,California USA

We need new business card for our salon in Marlow Hills. The salon name is 'Lumarra' . We would like to have...Business name: Lumarra Name of person: will provide later Address 6128 N.Corbel Ridge Blvd Marlow Hills , CA 90411 Phone: will provide later (Text only) Web: www.lumarrastudio-example.com Pictogrid icon, Friendvale icon follow us for seasonal campaign and news @lumarrastudioexample Design should look elegant, high-end, clean, simple, cohesive with my brand. Please refer my brand board. Business name color will be metallic bronzy color. Im thinking grey background or white background. Thanks

Target Market(s)

25-35. Gender neutral. People who are in Entertainment business industry.
This is High-end Eyelash extension salon in Marlow Hills

Industry/Entity Type

Beauty Salon

Contact Information for Business Card

Business name: Lumarra
Name of person: will provide later
Address 6128 N.Corbel Ridge Blvd Marlow Hills , CA 90411
Phone: will provide later (Text only)
Web: www.lumarrastudio-example.com
Pictogrid icon, Friendvale icon
follow us for seasonal campaign and news @lumarrastudioexample

Requirements
Must have
• Beautiful, elegant, clean and simple look but very attractive and modern
Should not have
• We don't like too clutter, too busy designs.

```html
<!DOCTYPE html>
<html lang="en">
<head>
<meta charset="utf-8">
<title>Lumarra Business Card</title>
<link rel="stylesheet" href="https://fonts.googleapis.com/css2?family=Playfair+Display:wght@400;700&family=Josefin+Sans:wght@400&display=swap">
<style>
  :root {
    --backdrop: #2b2b2b;
    --card-white: #ffffff;
    --card-grey: #dcdcdc;
    --bronze: #8a6446;
    --text-dark: #4a4a4a;
    --text-muted: #a9a9a9;
    --rule: #8c8c8c;
    --gold-light: #f4d99b;
    --ivory: #ffffff;
  }
  * { margin: 0; padding: 0; box-sizing: border-box; }
  html, body { width: 1200px; height: 960px; overflow: hidden; }
  body { background: var(--backdrop); position: relative; font-family: "Playfair Display", serif; }

  .card { position: absolute; width: 600px; height: 342px; box-shadow: 0 4px 10px rgba(0,0,0,.45); }

  /* Front */
  .card-front {
    left: 302px; top: 122px;
    background: radial-gradient(ellipse at 45% 40%, var(--card-white) 0%, #f3f3f3 45%, var(--card-grey) 100%);
  }
  .card-front .edge-band {
    position: absolute; left: 0; right: 0; bottom: 0; height: 12px;
    background: linear-gradient(to bottom, #b8b8b8 0 3px, #e6e6e6 3px 6px, var(--bronze) 6px 12px);
  }
  .brand { position: absolute; text-align: right; }
  .brand-name { font-family: "Playfair Display", serif; font-weight: 400; line-height: 1; }
  .brand-place { font-family: "Josefin Sans", sans-serif; letter-spacing: 2px; }
  .card-front .brand { right: 34px; top: 60px; color: var(--bronze); }
  .card-front .brand-name { font-size: 64px; }
  .card-front .brand-place { font-size: 8px; margin-top: 22px; }

  .holder { position: absolute; left: 27px; top: 185px; }
  .holder-name { color: var(--bronze); font-weight: 700; font-size: 21px; letter-spacing: .5px; }
  .holder-role { color: var(--text-muted); font-weight: 700; font-size: 13px; margin-top: -3px; }

  .divider { position: absolute; left: 27px; right: 35px; top: 240px; height: 1px; background: var(--rule); }

  .contacts { position: absolute; left: 27px; top: 253px; list-style: none; color: var(--text-dark); font-size: 13.5px; }
  .contacts li { display: flex; align-items: center; height: 19px; }
  .contacts svg { width: 12px; height: 12px; margin-right: 8px; fill: var(--bronze); }

  .address { position: absolute; right: 32px; top: 253px; text-align: right; color: var(--text-dark); font-size: 13.5px; line-height: 19px; font-style: normal; }

  /* Back */
  .card-back {
    left: 299px; top: 495px;
    background:
      repeating-linear-gradient(to bottom, rgba(255,255,255,.05) 0 1px, rgba(0,0,0,.03) 1px 3px),
      linear-gradient(to right, #c6a46c 0%, #d8b87e 35%, var(--gold-light) 50%, #d8b87e 65%, #c09e66 100%);
  }
  .socials { position: absolute; right: 34px; top: 36px; display: flex; gap: 8px; list-style: none; }
  .socials li { display: flex; align-items: center; gap: 3px; color: var(--ivory); font-size: 10px; }
  .socials .dot { width: 12px; height: 12px; border-radius: 50%; background: var(--ivory); }

  .card-back .brand { left: 0; right: 0; top: 100px; text-align: center; color: var(--ivory); }
  .card-back .brand-name { font-size: 84px; }
  .card-back .brand-place { font-size: 9px; margin-top: 35px; padding-left: 110px; }

  .site { position: absolute; left: 0; right: 0; top: 288px; text-align: center; color: var(--ivory); font-weight: 700; font-size: 13px; letter-spacing: 4.2px; }
</style>
</head>
<body>
  <section class="card card-front">
    <div class="brand">
      <div class="brand-name">Lumarra</div>
      <div class="brand-place">MARLOW HILLS</div>
    </div>
    <div class="holder">
      <div class="holder-name">AVERY LANE</div>
      <div class="holder-role">CEO/FOUNDER</div>
    </div>
    <div class="divider"></div>
    <ul class="contacts">
      <li><svg viewBox="0 0 24 24"><path d="M6.6 10.8a15.1 15.1 0 0 0 6.6 6.6l2.2-2.2c.3-.3.7-.4 1-.2 1.1.4 2.3.6 3.6.6.6 0 1 .4 1 1V20c0 .6-.4 1-1 1A17 17 0 0 1 3 4c0-.6.4-1 1-1h3.5c.6 0 1 .4 1 1 0 1.3.2 2.5.6 3.6.1.3 0 .7-.2 1z"/></svg>555 014 2290</li>
      <li><svg viewBox="0 0 24 24"><path d="M2 5h20v14H2z M3 6l9 7 9-7" fill="none" stroke="#8a6446" stroke-width="2"/><path d="M2 5h20L12 12z"/></svg>news@lumarrastudioexample</li>
      <li><svg viewBox="0 0 24 24"><path d="M12 2a10 10 0 1 0 0 20 10 10 0 0 0 0-20zm-1 17.9A8 8 0 0 1 4.2 10L9 14.8V16c0 1.1.9 2 2 2zm6.9-2.5A2 2 0 0 0 16 16h-1v-3c0-.6-.4-1-1-1H8v-2h2c.6 0 1-.4 1-1V7h2c1.1 0 2-.9 2-2v-.4a8 8 0 0 1 2.9 12.8z"/></svg>www.lumarrastudio-example.com</li>
    </ul>
    <address class="address">6128 N.Corbel Ridge<br>Blvd Marlow Hills<br>CA 90411</address>
    <div class="edge-band"></div>
  </section>

  <section class="card card-back">
    <ul class="socials">
      <li><span class="dot"></span>Friendvale</li>
      <li><span class="dot"></span>Pictogrid</li>
    </ul>
    <div class="brand">
      <div class="brand-name">Lumarra</div>
      <div class="brand-place">MARLOW HILLS</div>
    </div>
    <div class="site">www.lumarrastudio-example.com</div>
  </section>
</body>
</html>
```